Meadowlark Learning Growth Partners (MLGP)

This is a professional business card. Logo and picture are a must on the front of the card. I am an educational consultant. I have been consulting for the past three years for a company. I am now opening my own company. My goal for my consulting company is to eventually consult all over America.

Target Market(s)

Educators, schools, professionals

Industry/Entity Type

Consulting

Contact Information for Business Card

Picture/logo on front, simple modern design

Font styles to use
Serif

Colors
85abd2
0355a3
3176b5
cedeed

Requirements
Must have
• picture, logo,
• Odessa Pruitt, Ed.S
• address 5073 Cormorant ridge Dr. Nashville, TN 37940
• Cell:616-555-0148
• Office: 629-555-0172
• www.Mlgpedu.example
• pruittodessa@mailbox.example

```html
<!DOCTYPE html>
<html lang="en">
<head>
<meta charset="utf-8">
<title>Meadowlark Learning Growth Partners – Business Card</title>
<link rel="stylesheet" href="https://fonts.googleapis.com/css2?family=Alegreya:wght@500&family=Lexend:wght@500;600&family=Tinos&display=swap">
<style>
  :root {
    --backdrop: #d9d4cc;
    --blue-deep: #0b3b8c;
    --blue-mid: #0355a3;
    --blue-bright: #3176b5;
    --blue-soft: #85abd2;
    --blue-pale: #cedeed;
    --navy-ink: #0d3a84;
    --white: #ffffff;
    --card-white: #f7f8fa;
    --faint-mark: rgba(206, 222, 237, 0.55);
  }
  * { margin: 0; padding: 0; box-sizing: border-box; }
  html, body { width: 900px; height: 1200px; overflow: hidden; }
  body { background: var(--backdrop); position: relative; }

  .card {
    position: absolute;
    left: 88px;
    width: 732px;
    height: 428px;
    border-radius: 20px;
    overflow: hidden;
    box-shadow: 0 6px 14px rgba(0, 0, 0, 0.35);
  }
  .card-front {
    top: 137px;
    background: radial-gradient(circle at 60% 45%, var(--blue-bright) 0%, var(--blue-mid) 45%, var(--blue-deep) 100%);
    color: var(--white);
  }
  .card-back {
    top: 634px;
    background: linear-gradient(135deg, var(--white) 0%, var(--card-white) 60%, #eceef2 100%);
    color: var(--navy-ink);
  }

  .faint-mark {
    position: absolute;
    border-radius: 50%;
  }
  .card-front .faint-mark {
    left: 250px; top: 80px; width: 300px; height: 300px;
    border: 34px solid rgba(133, 171, 210, 0.18);
  }
  .card-back .faint-mark {
    left: 430px; top: 110px; width: 260px; height: 260px;
    border: 30px solid var(--faint-mark);
  }

  .brand {
    position: absolute;
    display: flex;
    align-items: center;
  }
  .brand-dot {
    width: 34px; height: 34px;
    border-radius: 50%;
    background: currentColor;
    margin-right: 14px;
  }
  .brand-initials {
    font-family: "Lexend", sans-serif;
    font-weight: 600;
    font-size: 38px;
    letter-spacing: 2px;
    line-height: 1;
  }
  .brand-rule {
    width: 2px;
    height: 98px;
    background: currentColor;
    margin: 0 14px 0 16px;
  }
  .brand-name {
    font-family: "Lexend", sans-serif;
    font-weight: 600;
    font-size: 19.5px;
    line-height: 26px;
  }
  .card-front .brand { left: 42px; top: 44px; }
  .card-back .brand { left: 152px; top: 160px; }

  .person-name {
    position: absolute;
    left: 40px; top: 182px;
    font-family: "Alegreya", serif;
    font-weight: 500;
    font-size: 30px;
  }

  .contact-list {
    position: absolute;
    left: 42px; top: 242px;
    list-style: none;
    font-family: "Tinos", serif;
    font-size: 15.5px;
  }
  .contact-list li {
    display: flex;
    align-items: center;
    height: 24.5px;
  }
  .contact-list li.address { margin-top: 16px; }
  .contact-list svg {
    width: 16px; height: 16px;
    margin-right: 11px;
    fill: none;
    stroke: var(--white);
    stroke-width: 1.6;
  }
  .contact-list svg .solid { fill: var(--white); stroke: none; }

  .portrait {
    position: absolute;
    left: 432px; top: 22px; right: 0; bottom: 0;
    background:
      radial-gradient(ellipse 70px 90px at 150px 110px, #e6c9a8 0%, rgba(230, 201, 168, 0) 100%),
      linear-gradient(180deg, rgba(3, 85, 163, 0) 0%, rgba(30, 30, 40, 0.5) 55%, #1c1f2a 100%);
  }
</style>
</head>
<body>

<section class="card card-front">
  <div class="faint-mark"></div>

  <div class="brand">
    <span class="brand-dot"></span>
    <span class="brand-initials">MLGP</span>
    <span class="brand-rule"></span>
    <span class="brand-name">Meadowlark<br>Learning<br>Growth<br>Partners</span>
  </div>

  <h1 class="person-name">Odessa Pruitt, Ed.S</h1>

  <ul class="contact-list">
    <li>
      <svg viewBox="0 0 16 16"><rect x="3.5" y="1" width="9" height="14" rx="1.5"/><line x1="7" y1="12.5" x2="9" y2="12.5"/></svg>
      616-555-0148
    </li>
    <li>
      <svg viewBox="0 0 16 16"><path class="solid" d="M1 6c0-2 3-3 7-3s7 1 7 3v1h-3.5V5.5h-7V7H1z"/><path class="solid" d="M3.5 8h9l1.5 6H2z"/></svg>
      629-555-0172
    </li>
    <li>
      <svg viewBox="0 0 16 16"><circle cx="8" cy="8" r="6.5"/><ellipse cx="8" cy="8" rx="2.8" ry="6.5"/><line x1="1.5" y1="8" x2="14.5" y2="8"/></svg>
      www.Mlgpedu.example
    </li>
    <li>
      <svg viewBox="0 0 16 16"><rect x="1.5" y="3.5" width="13" height="9"/><polyline points="1.5,3.5 8,9 14.5,3.5"/></svg>
      pruittodessa@mailbox.example
    </li>
    <li class="address">
      <svg viewBox="0 0 16 16"><path class="solid" d="M8 1a5 5 0 0 1 5 5c0 3.5-5 9-5 9S3 9.5 3 6a5 5 0 0 1 5-5zm0 3a2 2 0 1 0 0 4 2 2 0 0 0 0-4z"/></svg>
      5073 Cormorant ridge Dr. Nashville, TN 37940
    </li>
  </ul>

  <div class="portrait" role="img" aria-label="Portrait photo of Odessa Pruitt in a dark blazer and white blouse"></div>
</section>

<section class="card card-back">
  <div class="faint-mark"></div>
  <div class="brand">
    <span class="brand-dot"></span>
    <span class="brand-initials">MLGP</span>
    <span class="brand-rule"></span>
    <span class="brand-name">Meadowlark<br>Learning<br>Growth<br>Partners</span>
  </div>
</section>

</body>
</html>
```